Corrow Family Farm fresh honey jar label

I need a label for jars of honey harvested at our farm. These are for gifts and personal use. We are looking to incorporate our farm brand into the label. We would like the design to take the existing brand and add some element like bees, honey, flowers, or hives to indicate the contents. We want the design to feel homemade and authentic without feeling cheap or hoaky

Requirements
Must have
• The label must be made to fit a 1" x2" rectangular label. The label must include the attached family brand. The label must include the text "Corrow Family Farms" "Pinebrook, USA" "Farm Fresh Honey". The label will be printed on off-white paper
Nice to have
• It would be nice to have illustrations of bees or flowers around the logo or hives or honeycombs. The label should have a vintage feel
Should not have
• The label should not feel overly cartoonish or hoaky

```html
<!DOCTYPE html>
<html lang="en">
<head>
<meta charset="utf-8">
<title>Corrow Family Farms – Farm Fresh Honey Label</title>
<link rel="stylesheet" href="https://fonts.googleapis.com/css2?family=Josefin+Sans:wght@400;600&family=Libre+Caslon+Text:wght@400&display=swap">
<style>
  :root {
    --backdrop: #ababab;
    --paper: #fdf7ee;
    --panel: #ffffff;
    --ink: #0d0d0d;
    --reverse: #ffffff;
    --comb: #1a1a1a;
  }
  * { box-sizing: border-box; margin: 0; padding: 0; }
  html, body {
    width: 1200px; height: 1090px; overflow: hidden;
    background: var(--backdrop);
  }
  .label {
    position: absolute; left: 350px; top: 45px;
    width: 500px; height: 1000px;
    background: var(--paper);
    font-family: "Josefin Sans", sans-serif;
    color: var(--ink);
  }
  .label__frame {
    position: absolute; left: 26px; top: 24px;
    width: 452px; height: 923px;
    background: var(--panel);
    border: 2px solid var(--ink);
    border-radius: 28px;
  }
  .brand-mark {
    position: absolute; left: 0; width: 100%; top: 150px;
    text-align: center;
    font-family: "Josefin Sans", sans-serif;
    font-weight: 600; font-size: 64px; letter-spacing: 10px;
    color: var(--ink);
  }
  .farm-name {
    position: absolute; left: 0; width: 100%; top: 356px;
    text-align: center; font-size: 23px; font-weight: 400; letter-spacing: 4.5px;
  }
  .farm-place {
    position: absolute; left: 0; width: 100%; top: 389px;
    text-align: center; font-size: 17px; font-weight: 600; letter-spacing: 3.5px;
  }
  .divider {
    position: absolute; left: 100px; top: 434px;
    width: 302px; height: 2px; background: var(--ink);
  }
  .honeycomb-art {
    position: absolute; left: 151px; top: 436px;
    width: 204px; height: 200px;
    background: linear-gradient(180deg, var(--comb) 0%, #3a3a3a 100%);
    border-radius: 0 0 40px 40px;
  }
  .product-kicker {
    position: absolute; left: 0; width: 100%; top: 670px;
    text-align: center; font-size: 23px; font-weight: 400; letter-spacing: 7px;
  }
  .product-band {
    position: absolute; left: 26px; top: 702px;
    width: 452px; height: 104px;
    background: var(--ink);
    display: flex; align-items: center; justify-content: center;
  }
  .product-name {
    font-family: "Libre Caslon Text", serif;
    font-size: 84px; line-height: 1; letter-spacing: 2px;
    color: var(--reverse); padding-top: 8px;
  }
  .product-claim {
    position: absolute; left: 0; width: 100%; top: 818px;
    text-align: center; font-size: 14px; font-weight: 600; letter-spacing: 2.6px;
  }
  .origin-badge {
    position: absolute; left: 0; top: 890px; width: 500px; height: 100px;
  }
</style>
</head>
<body>
  <main class="label">
    <div class="label__frame"></div>

    <div class="brand-mark">CORROW</div>

    <p class="farm-name">CORROW FAMILY FARMS</p>
    <p class="farm-place">PINEBROOK, USA</p>

    <div class="divider"></div>
    <div class="honeycomb-art" role="img" aria-label="Black honeycomb cells dripping honey, with small bees flying around"></div>

    <p class="product-kicker">FARM FRESH</p>
    <div class="product-band"><h1 class="product-name">HONEY</h1></div>
    <p class="product-claim">100% NATUAL FARM PRODUCT</p>

    <svg class="origin-badge" viewBox="0 0 500 100" aria-hidden="true">
      <line x1="152" y1="48" x2="212" y2="48" stroke="#0d0d0d" stroke-width="2"/>
      <line x1="288" y1="48" x2="348" y2="48" stroke="#0d0d0d" stroke-width="2"/>
      <circle cx="250" cy="48" r="44" fill="#ffffff"/>
      <circle cx="250" cy="52" r="28" fill="none" stroke="#0d0d0d" stroke-width="4"/>
      <circle cx="250" cy="52" r="20" fill="#0d0d0d"/>
    </svg>
  </main>
</body>
</html>
```